Website design to promote trampoline business

We require a website design for our business. The business is primarily provising access for people between 5YO and 40YO to jump on trampolines for fun and fitness.

We have a logo and color schemes already and the website should incorporate these colors and designs.

We would like to incorporate the following pages:-

Book Now!
Home
About Us
Locations & Hours
Jumping
Groups & Events
Gallery
Safety
Latest News
Careers

Industry/Entity Type

Business

Requirements
Must have
• Incorporate our logo and colors (files attached).

```html
<!DOCTYPE html>
<html lang="en">
<head>
<meta charset="utf-8">
<title>Bounce Yard Trampolines</title>
<link href="https://fonts.googleapis.com/css2?family=Cabin:wght@400;500;600&display=swap" rel="stylesheet">
<style>
:root{
  --orange:#f27c00;
  --blue:#27a8d8;
  --sky:#d9edfa;
  --sky-deep:#d3e8f8;
  --ink:#2b2b2b;
  --text:#444;
  --footer:#333333;
  --footer-band:#9a9a9a;
  --white:#fff;
}
*{box-sizing:border-box;margin:0;padding:0}
html,body{width:739px;height:1200px;overflow:hidden}
body{font-family:"Cabin",sans-serif;color:var(--text);background:var(--white);position:relative}
.abs{position:absolute}

/* header */
.site-header{position:absolute;left:0;top:0;width:739px;height:78px;background:var(--sky);border-top:3px solid var(--blue)}
.brand{position:absolute;left:106px;top:14px;display:flex;align-items:center;gap:8px}
.brand-mark{width:14px;height:14px;background:var(--blue)}
.brand-name{font-size:21px;font-weight:600;color:var(--blue);line-height:1;letter-spacing:.5px}
.book-now{position:absolute;left:553px;top:0;width:75px;height:18px;background:var(--blue);color:var(--white);font-size:9.5px;font-weight:600;text-align:center;line-height:18px;border-radius:0 0 8px 8px}
.top-links{position:absolute;left:443px;top:39px;font-size:8.5px;color:var(--ink)}
.top-phone{position:absolute;left:541px;top:35px;font-size:12.5px;color:var(--ink);display:flex;align-items:center;gap:6px}

/* nav */
.main-nav{position:absolute;left:0;top:78px;width:739px;height:23px;background:var(--orange);display:flex;padding-left:98px}
.main-nav a{color:var(--white);font-size:8.5px;text-decoration:none;line-height:23px;padding:0 14px 0 11px;position:relative}
.main-nav a::after{content:"";position:absolute;right:0;top:2px;width:8px;height:19px;border-right:1.5px solid rgba(255,255,255,.45);border-radius:0 10px 10px 0}

/* hero */
.hero{position:absolute;left:0;top:101px;width:739px;height:277px;background:linear-gradient(180deg,#a9b7be 0%,#8c9a7c 40%,#5e7a3a 75%,#3f5a2a 100%)}
.hero-caption{position:absolute;left:0;bottom:0;width:739px;height:44px;background:rgba(30,30,30,.72)}
.hero-caption p{position:absolute;left:118px;top:14px;font-size:13px;color:var(--white)}
.hero-arrows{position:absolute;left:592px;top:14px;display:flex;gap:3px}
.arrow-box{width:19px;height:17px;background:#111;display:flex;align-items:center;justify-content:center}
.orange-rule{position:absolute;left:0;top:378px;width:739px;height:3px;background:var(--orange)}

/* welcome */
.welcome{position:absolute;left:0;top:381px;width:739px;height:202px;background:#f6fbfe;text-align:center}
.welcome h1{font-size:28px;font-weight:400;color:var(--orange);margin-top:27px;letter-spacing:.5px}
.welcome .lead{font-size:10.5px;color:var(--ink);margin-top:4px}
.welcome .body{font-size:6.6px;line-height:9px;width:505px;margin:12px auto 0;color:var(--text)}
.read-more{font-size:6.8px;font-weight:600;color:var(--orange);display:inline-block;margin-top:25px}

/* gallery */
.gallery{position:absolute;left:0;top:583px;width:739px;height:205px;background:var(--sky-deep)}
.gallery h2{position:absolute;left:0;width:739px;top:26px;text-align:center;font-size:26px;font-weight:400;color:var(--ink)}
.gallery-arrows{position:absolute;left:582px;top:28px;display:flex;gap:4px}
.outline-arrow{width:23px;height:23px;border:1px solid #333;display:flex;align-items:center;justify-content:center}
.thumb{position:absolute;top:77px;width:123px;height:100px;border:3px solid var(--orange)}
.blue-rule{position:absolute;left:0;top:788px;width:739px;height:4px;background:var(--blue)}

/* info */
.section-title{position:absolute;font-size:17.5px;font-weight:400;color:var(--blue)}
.event{position:absolute;left:105px;width:260px;height:52px}
.event-photo{position:absolute;left:0;top:0;width:81px;height:50px;box-shadow:0 1px 3px rgba(0,0,0,.35)}
.event h3{position:absolute;left:89px;top:2px;font-size:8.5px;font-weight:600;color:var(--orange)}
.event p{position:absolute;left:89px;top:14px;font-size:6.6px;line-height:9px;width:165px;color:var(--text)}
.view-more{position:absolute;font-size:6.8px;font-weight:600;color:var(--blue)}
.divider{position:absolute;left:369px;top:830px;width:1px;height:206px;background:#dcdcdc}
.label{position:absolute;left:384px;font-size:8.5px;font-weight:600;color:var(--orange)}
.hours{position:absolute;left:405px;top:893px;width:190px;font-size:6.8px;color:var(--ink)}
.hours div{display:flex;justify-content:space-between;height:16px;line-height:14px;border-bottom:1px solid #e2e2e2}
.hours div:last-child{border-bottom:0}
.address{position:absolute;left:405px;top:964px;font-size:6.8px;line-height:15.5px;color:var(--ink)}

/* footer */
.footer-band{position:absolute;left:0;top:1054px;width:739px;height:6px;background:var(--footer-band)}
.site-footer{position:absolute;left:0;top:1060px;width:739px;height:140px;background:var(--footer);color:var(--white)}
.foot-label{position:absolute;top:66px;font-size:12px;display:flex;align-items:center;gap:6px}
.foot-box{position:absolute;top:14px;height:120px;border:1px solid #555;border-left-width:1px}
.foot-list{position:absolute;font-size:7.5px;line-height:15.4px;list-style:none}
.foot-list li::before{content:"»";margin-right:6px;font-size:7px}
.contact-row{display:flex;align-items:center;gap:8px;font-size:7.5px;line-height:9px;margin-bottom:6px}
.social{position:absolute;left:423px;top:102px;display:flex;gap:9px}
.social span{width:11px;height:11px;border-radius:50%;background:#d8d8d8}
.foot-brand{position:absolute;left:553px;top:54px;font-size:15px;font-weight:600;color:#9a9a9a}
</style>
</head>
<body>

<header class="site-header">
  <div class="brand"><span class="brand-mark"></span><span class="brand-name">BOUNCE YARD</span></div>
  <div class="book-now">BOOK NOW !</div>
  <div class="top-links">About Us &nbsp;|&nbsp; Contact Us</div>
  <div class="top-phone">
    <svg width="11" height="11" viewBox="0 0 24 24"><path d="M6.6 10.8a15 15 0 006.6 6.6l2.2-2.2c.3-.3.7-.4 1-.2 1.1.4 2.3.6 3.6.6.6 0 1 .4 1 1V20c0 .6-.4 1-1 1A17 17 0 013 4c0-.6.4-1 1-1h3.5c.6 0 1 .4 1 1 0 1.3.2 2.5.6 3.6.1.3 0 .7-.2 1z" fill="#2b2b2b"/></svg>
    555 210 4477
  </div>
</header>

<nav class="main-nav">
  <a>Locations &amp; Hours</a><a>Jumping</a><a>Groups &amp; Events</a><a>Gallery</a><a>Safety</a><a>Latest News</a><a>Careers</a><a>Requirements</a>
</nav>

<section class="hero" role="img" aria-label="Photo of children jumping on a backyard trampoline">
  <div class="hero-caption">
    <p>The perfect family Trampoline , Great outdoor fun and fitness</p>
    <div class="hero-arrows">
      <span class="arrow-box"><svg width="6" height="9"><path d="M5 1L1 4.5 5 8" stroke="#fff" fill="none" stroke-width="1.4"/></svg></span>
      <span class="arrow-box"><svg width="6" height="9"><path d="M1 1l4 3.5L1 8" stroke="#fff" fill="none" stroke-width="1.4"/></svg></span>
    </div>
  </div>
</section>
<div class="orange-rule"></div>
<svg class="abs" style="left:356px;top:381px" width="26" height="13"><path d="M0 0h26L13 13z" fill="#f27c00"/></svg>

<section class="welcome">
  <h1>WELCOME</h1>
  <p class="lead">Nulla vitae ligula rhoncus, tincidunt nulla eget, placerat est. Nulla rutrum non leo non fringilla.</p>
  <p class="body">Pellentesque pellentesque tellus ut magna consectetur, vitae lobortis tellus facilisis. Proin sed adipiscing magna, ac pulvinar nulla. Phasellus auctor faucibus leo, in venenatis purus bibendum id. Sed eget magna non nisl auctor ultricies. Nullam scelerisque eros non lacus tincidunt gravida. In imperdiet, lectus nec mollis egestas, mauris leo placerat mauris, ac ullamcorper mi purus id nibh. Nunc egestas lacus lacus, eget hendrerit augue tempor vel.</p>
  <p class="body" style="margin-top:8px">Nunc congue tempus felis sed euismod. Donec ornare sit amet elit a viverra.</p>
  <span class="read-more">READ MORE &nbsp;›</span>
</section>
<svg class="abs" style="left:356px;top:583px" width="26" height="12"><path d="M0 0h26L13 12z" fill="#f6fbfe"/></svg>

<section class="gallery">
  <h2>OUR GALLERY</h2>
  <div class="gallery-arrows">
    <span class="outline-arrow"><svg width="7" height="11"><path d="M6 1L1.5 5.5 6 10" stroke="#222" fill="none" stroke-width="1.5"/></svg></span>
    <span class="outline-arrow"><svg width="7" height="11"><path d="M1 1l4.5 4.5L1 10" stroke="#222" fill="none" stroke-width="1.5"/></svg></span>
  </div>
  <div class="thumb" style="left:106px;background:linear-gradient(180deg,#8fae6a,#c9c2b4)" role="img" aria-label="Gallery photo of kids playing on a ground trampoline"></div>
  <div class="thumb" style="left:241px;background:linear-gradient(180deg,#4f6d3c,#2f3d32)" role="img" aria-label="Gallery photo of children inside a netted trampoline"></div>
  <div class="thumb" style="left:376px;background:linear-gradient(180deg,#6d8a4a,#9a9e96)" role="img" aria-label="Gallery photo of a family on a round trampoline"></div>
  <div class="thumb" style="left:512px;background:linear-gradient(180deg,#6fa7e0,#4e8a3a)" role="img" aria-label="Gallery photo of a girl jumping in a trampoline enclosure"></div>
</section>
<div class="blue-rule"></div>
<svg class="abs" style="left:356px;top:792px" width="26" height="12"><path d="M0 0h26L13 12z" fill="#27a8d8"/></svg>

<h2 class="section-title" style="left:107px;top:836px">GROUPS &amp; EVENTS</h2>
<div class="event" style="top:879px">
  <div class="event-photo" style="background:linear-gradient(180deg,#3d4f6a,#8a5a4a)" role="img" aria-label="Photo of a large group event indoors"></div>
  <h3>Tincidunt nulla eget</h3>
  <p>Proin sed adipiscing magna, ac pulvinar nulla. Phasellus auctor faucibus leo, in venenatis purus bibendum id.</p>
</div>
<div class="event" style="top:948px">
  <div class="event-photo" style="background:linear-gradient(180deg,#6fa048,#4a7ab0)" role="img" aria-label="Photo of a group of children outdoors"></div>
  <h3>Tincidunt nulla eget</h3>
  <p>Proin sed adipiscing magna, ac pulvinar nulla. Phasellus auctor faucibus leo, in venenatis purus bibendum id.</p>
</div>
<span class="view-more" style="left:307px;top:1023px">VIEW MORE &nbsp;›</span>

<div class="divider"></div>

<h2 class="section-title" style="left:382px;top:836px">LOCATIONS &amp; HOURS</h2>
<span class="label" style="top:882px">Hours</span>
<div class="hours">
  <div><span>Mon, Tues &amp; Wed</span><span>Noon – 8pm</span></div>
  <div><span>Thurs, Fri &amp; Sat</span><span>Noon – 9pm</span></div>
  <div><span>Sunday</span><span>Noon – 7pm</span></div>
</div>
<span class="label" style="top:950px">Locations</span>
<div class="address">
  1200 Elm Row, 4410 – 4420 Mill Road<br>
  Northfield, AB12 3CD. Westbury, EF45 6GH<br>
  Phone: +1 800 555 0142 Phone: +1 800 555 0142
</div>
<span class="view-more" style="left:575px;top:1023px">VIEW MORE &nbsp;›</span>

<div class="footer-band"></div>
<svg class="abs" style="left:356px;top:1060px" width="26" height="13"><path d="M0 0h26L13 13z" fill="#9a9a9a"/></svg>
<footer class="site-footer">
  <div class="foot-label" style="left:109px">Sitemap <svg width="6" height="10"><path d="M0 0l6 5-6 5z" fill="#fff"/></svg></div>
  <div class="foot-box" style="left:159px;width:212px;border-right:0"></div>
  <ul class="foot-list" style="left:175px;top:22px">
    <li>Home</li><li>About Us</li><li>Apply Now</li><li>Locations &amp; Hours</li><li>Jumping</li><li>Groups &amp; Events</li>
  </ul>
  <ul class="foot-list" style="left:264px;top:22px">
    <li>Gallery</li><li>Safety</li><li>Latest News</li><li>Careers</li><li>Requirements</li><li>Contact Us</li>
  </ul>
  <div class="foot-label" style="left:341px">Contact <svg width="6" height="10"><path d="M0 0l6 5-6 5z" fill="#fff"/></svg></div>
  <div class="foot-box" style="left:390px;width:145px;border-right:0"></div>
  <div class="abs" style="left:402px;top:28px">
    <div class="contact-row"><svg width="9" height="9" viewBox="0 0 10 10"><path d="M5 1L1 5h1.5v4h5V5H9z" fill="#fff"/></svg><span>Harbor Lane suite 4 Fairview<br>CA 90210</span></div>
    <div class="contact-row"><svg width="9" height="9" viewBox="0 0 24 24"><path d="M6.6 10.8a15 15 0 006.6 6.6l2.2-2.2c.3-.3.7-.4 1-.2 1.1.4 2.3.6 3.6.6.6 0 1 .4 1 1V20c0 .6-.4 1-1 1A17 17 0 013 4c0-.6.4-1 1-1h3.5c.6 0 1 .4 1 1 0 1.3.2 2.5.6 3.6.1.3 0 .7-.2 1z" fill="#fff"/></svg>555 210 4477</div>
    <div class="contact-row"><svg width="9" height="9" viewBox="0 0 10 10"><path d="M2.5 1h5v2h-5zM1 3.5h8v4H7.5V9h-5V7.5H1z" fill="#fff"/></svg>888 555 0190</div>
    <div class="contact-row"><svg width="9" height="8" viewBox="0 0 10 8"><rect x=".5" y=".5" width="9" height="7" fill="#fff"/><path d="M.5.5l4.5 4 4.5-4" stroke="#333" fill="none"/></svg>hello@bounceyard.example</div>
  </div>
  <div class="social" aria-label="Social links"><span></span><span></span><span></span></div>
  <div class="foot-brand">BOUNCE YARD</div>
</footer>

</body>
</html>
```